I work in creative/artistic projects across different mediums.
It needs to communicate creativity, style, sexy, uniqueness, individuality and sophistication.
It should not look corporate.
Colours I like are black silver gold deep purple, chocolate, orchid.
It doesn't have to make use of all these colours.
I do not like bright primary colors.
Updates

Project Deadline Extended
Reason: Still in the communication process and to allow the person enough time to finish the design. Though i should know in the next day or two. Thank you.

Target Market(s)

creatives and companies wanting to inject creativity into thier business.

Industry/Entity Type

Work

Contact Information for Business Card

Marcus Tellwick
0418592036
marcus@marcustellwick.com

quietgoldenhour.com.au

Requirements
Should not have
• Anything corporate OR OLD FASHIONED

```html
<!DOCTYPE html>
<html lang="en">
<head>
<meta charset="utf-8">
<title>Marcus Tellwick — Business Card</title>
<link rel="stylesheet" href="https://fonts.googleapis.com/css2?family=Italianno&family=Open+Sans:wght@400&family=Questrial&display=swap">
<style>
  :root {
    --backdrop: #8c8c8c;
    --card-black: #0b0b0b;
    --card-edge: #1c1c1c;
    --gold-light: #e9d3a4;
    --gold-mid: #b8945c;
    --gold-dark: #6b5230;
    --silver-text: #e6e6e6;
  }
  html, body {
    margin: 0;
    padding: 0;
    width: 1200px;
    height: 1200px;
    overflow: hidden;
    background: var(--backdrop);
  }
  .sheet {
    width: 1200px;
    height: 1200px;
    display: flex;
    flex-direction: column;
    align-items: center;
    justify-content: center;
    gap: 52px;
  }
  .card {
    position: relative;
    width: 900px;
    height: 514px;
    background: radial-gradient(ellipse at 50% 40%, var(--card-edge) 0%, var(--card-black) 70%);
    box-shadow: 0 10px 30px rgba(0, 0, 0, 0.35);
    overflow: hidden;
  }
  .gold-text {
    background: linear-gradient(100deg, var(--gold-dark) 0%, var(--gold-light) 35%, var(--gold-mid) 60%, var(--gold-light) 85%, var(--gold-dark) 100%);
    -webkit-background-clip: text;
    background-clip: text;
    color: transparent;
  }

  /* Front face */
  .front-name {
    position: absolute;
    left: 0;
    right: 0;
    top: 168px;
    text-align: center;
    font-family: "Italianno", cursive;
    font-size: 104px;
    letter-spacing: 10px;
    line-height: 1;
    padding-left: 60px;
  }

  /* Back face */
  .contact-list {
    position: absolute;
    left: 70px;
    top: 180px;
    margin: 0;
    padding: 0;
    list-style: none;
    font-family: "Open Sans", sans-serif;
    font-size: 19px;
    line-height: 38px;
    color: var(--silver-text);
  }
  .contact-list .label {
    margin-right: 6px;
  }
  .gold-rule {
    position: absolute;
    left: 452px;
    top: 150px;
    width: 3px;
    height: 250px;
    background: linear-gradient(180deg, var(--gold-light) 0%, var(--gold-mid) 50%, var(--gold-dark) 100%);
  }
  .back-name {
    position: absolute;
    left: 500px;
    top: 258px;
    margin: 0;
    font-family: "Questrial", sans-serif;
    font-weight: 400;
    font-size: 26px;
    letter-spacing: 4px;
    color: var(--silver-text);
    white-space: nowrap;
  }
</style>
</head>
<body>
  <main class="sheet">
    <section class="card card-front" aria-label="Card front">
      <div class="front-name gold-text">Marcus Tellwick</div>
    </section>

    <section class="card card-back" aria-label="Card back">
      <ul class="contact-list">
        <li><span class="label">M:</span>0418592036</li>
        <li><span class="label">E:</span>marcus@marcustellwick.com</li>
        <li><span class="label">W:</span>quietgoldenhour.com.au</li>
      </ul>
      <div class="gold-rule"></div>
      <h1 class="back-name">MARCUS TELLWICK</h1>
    </section>
  </main>
</body>
</html>
```